Etiketten für Ätherische Öle, Extrakte und Speiseöle gesucht
Zielgruppe
Wir verkaufen natürlich Produkte. Ätherische öle, Extrakte, Speise öle.
Wir verkaufen im Webshop, Kaufwelt und auch im Betrieb.
https://www.natur-sefo.com
Wir verkaufen hauptsächlich innerhalb Italiens und Deutschland daher doppel sprachig.
Aufgabenstellung
Guten Tag
Bitte verwenden Sie! : * beispiel_10_ml_etikett_nachbau.jpg *
Da mir die kleinste Größe die wichtigste ist habe ich ein beispiel Hochgeladen. Das kleinste Etikett lässt sich öffnen und daher sind nur 7 cm ersichtlich und man muss das Etikett aufmachen.
Habe ein Beispiel Hochgeladen. Aber bitte einfach kreativ sein. *Anhang: beispiel Etikett*
Sobald ich eine Art vom kelinsten habe würde ich dies für die 2 anderen Größen übernehmen aber das man Sie irgendwie gut unterscheiden kann da dies dann komplett andere Produkte (Extrakte/Speise öl) sein werden.
Erstellung von drei unterschiedlichen Größen von Etiketten mit folgenden Eigenschaften:
Am wichtigsten ist mir das kleinste Etikett da dies auch am schwersten ist daher habe ich die anderen Größen nun gelöscht!
• 10 ml Länge: 155 mm Breite: 32 mm.
Brauche 3 unterschiedliche Grund Farben: z. B. Ätherische Öle (Grün) Extrakte (Rot) Speiseöle (gelb). Die Farben lasse ich sie entscheiden.
Die Etiketten müssen 2 Sprachen (Deutsch / Italienisch) sein deshalb muss dieses berücksichtigt werden.
Anbei finden Sie:
• Logo (Bild Logo)
• Beispiel Text ätherische Öle
• Bilder der aktuellen Flaschen
Unter https://www.natur-sefo.com/de finden Sie meine Seite
Anmerkung: Im Anhang: *Back*
Habe ich mein Logo mit Firmennamen ; Bio des Hollmer Tobias
Da ich jedoch nicht alle Produkte im biologischen Anbau habe und mein Logo zu miss Verständnis führen könnte habe ich ein Bildliches Logo gemacht das ich fortan auf meinen Produkten haben möchte. Im besonderes dieses Grün das in beiden vorhanden ist versuche ich zu integrieren.
Habe selbst ein Etikett designet das aber sehr unprofessionell wirkt aber dieses Grüne das ich gerne als merkmal unterbringen würde.
Siehe Anhang: neemöl

```html
<!DOCTYPE html>
<html lang="de">
<head>
<meta charset="utf-8">
<title>Lavendel Fein – Etikett 10 ml</title>
<link rel="stylesheet" href="https://fonts.googleapis.com/css2?family=Delius&family=Roboto:wght@400&family=Roboto+Condensed:wght@400;700&display=swap">
<style>
  :root {
    --page-bg: #f3f3f3;
    --label-bg: #ffffff;
    --ink: #1c1c1c;
    --purple: #5a2d86;
    --lavender-light: #b7a6d9;
    --lavender-mid: #7b62b8;
    --stem-green: #8aa87a;
    --brand-green: #6dbb3c;
  }
  * { margin: 0; padding: 0; box-sizing: border-box; }
  html, body {
    width: 1200px; height: 1200px; overflow: hidden;
    background: var(--page-bg);
  }
  .label {
    position: absolute;
    left: 40px; top: 382px;
    width: 1120px; height: 437px;
    background: var(--label-bg);
    box-shadow: 0 2px 10px rgba(0,0,0,0.12);
    font-family: "Roboto Condensed", sans-serif;
    color: var(--ink);
  }
  .panel-left {
    position: absolute; left: 29px; top: 26px; width: 245px;
    font-size: 11px; line-height: 1.45;
  }
  .panel-left p { margin-bottom: 8px; }
  .producer { margin-top: 30px; }
  .producer strong { font-weight: 700; }
  .lot { margin-top: 18px; }
  .shelf-life {
    display: flex; align-items: flex-start; gap: 6px;
    margin-top: 14px; font-size: 10.5px; line-height: 1.25;
  }
  .shelf-life svg { flex: none; }
  .shelf-life strong { color: var(--purple); font-weight: 700; }
  .shelf-life .accent { color: var(--purple); }

  .panel-center {
    position: absolute; left: 360px; top: 0; width: 400px; height: 437px;
  }
  .lavender-art {
    position: absolute; left: 126px; top: 22px; width: 110px; height: 232px;
    background: linear-gradient(180deg, var(--lavender-mid) 0%, var(--lavender-light) 45%, var(--stem-green) 100%);
    border-radius: 55px 55px 10px 10px;
    opacity: 0.8;
  }
  .brand-badge {
    position: absolute; left: 246px; top: 30px;
  }
  .product-title {
    position: absolute; left: 0; top: 266px; width: 400px;
    text-align: center; white-space: nowrap;
    font-family: "Delius", cursive; font-weight: 400;
    font-size: 46px; line-height: 1;
    color: var(--purple);
  }
  .title-rule {
    position: absolute; left: 150px; top: 326px; width: 100px; height: 3px;
    background: var(--purple);
  }
  .botanical-name {
    position: absolute; left: 0; top: 342px; width: 400px;
    text-align: center;
    font-family: "Roboto", sans-serif;
    font-size: 16.5px; line-height: 1.18;
    color: var(--purple);
  }

  .panel-right {
    position: absolute; left: 832px; top: 26px; width: 270px;
    font-size: 11px; line-height: 1.55;
  }
  .panel-right p { margin-bottom: 6px; }
  .panel-right strong { font-weight: 700; }
  .panel-right .lang-block { margin-top: 20px; }
</style>
</head>
<body>
  <main class="label">
    <section class="panel-left">
      <p>Nur in der angegeben Verdünnung anwenden! Nicht in die Augen oder auf die Schleimhäute bringen! Außer Reichweite von Kindern lagern. Abgefüllt in Italien</p>
      <p>Da usare solo diluito come da indicazione! Evitare il contatto con occhi e mucose! Tenere fuori dalla portata dei bambini. Imbottigliato in Italy</p>
      <div class="producer">
        <strong>Bio des Hollmer Tobias</strong><br>
        Lindenweg 8<br>
        I-39020 Marling<br>
        IVA: IT01846350219<br>
        CF.: HLLTBS88M12F132Q<br>
        Tel: +39 0473/412788 Handy: 3471238856<br>
        www.natur-sefo.com<br>
        Info.natursefo@mail.com
      </div>
      <div class="lot">LottoNummer/CH nummer: 123456</div>
      <div class="shelf-life">
        <svg width="22" height="18" viewBox="0 0 22 18" aria-hidden="true">
          <path d="M3 7 h13 v4 a6.5 6 0 0 1 -13 0 z" fill="#5a2d86"/>
          <path d="M5 6 l4 -5 l4 5" fill="none" stroke="#5a2d86" stroke-width="1.6"/>
          <path d="M16 8 a3 3 0 0 1 0 5" fill="none" stroke="#5a2d86" stroke-width="1.6"/>
        </svg>
        <span><span class="accent">Haltbar bis</span> <strong>12 Monate</strong><br>nach der Öffnung</span>
      </div>
    </section>

    <section class="panel-center">
      <div class="lavender-art" role="img" aria-label="Aquarell-Illustration blühender Lavendelzweige"></div>
      <svg class="brand-badge" width="110" height="110" viewBox="0 0 110 110" role="img" aria-label="Markenzeichen">
        <circle cx="55" cy="55" r="52" fill="var(--brand-green)"/>
      </svg>
      <h1 class="product-title">Lavendel Fein</h1>
      <div class="title-rule"></div>
      <p class="botanical-name">Lavanda vera<br>Lavandula angustifolia</p>
    </section>

    <section class="panel-right">
      <p><strong>100% olio essenziale naturale.</strong> Cosmetico aromatico per la cura del corpo.</p>
      <p><strong>Modo d'uso:</strong> Come olio da massaggio o olio per il corpo: versare max. 15 gocce in 50ml di liquido p.es. olio di mandorla. Come bagnoschiuma: aggiungere 8-15 gocce versare nell acqua del bagno.</p>
      <p><strong>Ingredients:</strong> Lavandula angustifolia oil, Limonene*, Linalool*, geraniol*<br>
        *natürliche Bestandteile des etherischen Öls<br>
        * Olio essenziale con sostanze naturali</p>
      <div class="lang-block">
        <p><strong>100% natürliches etherisches Öl.</strong><br>Aroma-Kosmetikum zur Körperpflege.</p>
        <p><strong>Anwendung:</strong> Als Haut- u. Massageöl max 15 Tr. Mit 50 ml z.B. Mandelöl mischen. Als Badezusatz 8-15 Tr. Auf 4 EßL Sahne oder Milch ins Badewasser geben.</p>
      </div>
    </section>
  </main>
</body>
</html>
```